Additional page needed for existing website

I have an existing website www.quillofern.co.uk and I need two additional page adding to the website. We offer a service that allows a parent to understand what their children are doing online and block inappropriate content, its a "parental control" app. It currently only works with Kelos devices.
The features of the service are -
Block inappropriate content, we block over 100 million websites.
Set Device Access Times, you can set times that the device can access the Internet.
App Management, Quillo Fern will scan the device every hour and detect any risky apps that have been installed.
Dashboard shows what websites have been visited.

First page -
The new page will have a page name of "Qorra Parental Control App"
The meta title tag is "Qorra 6 Parental Control App | KELOS Parental Control App | Quillo Fern" and Meta Description Tag of "“If your child has an Qorra and you want to check which apps they mostly use then Install Quillo Fern Parental Control App for Qorra, Yarvo, and KELOS. Download Here."
We need content on the page of around 300-500 words. (keyword density should not be more than 2%)
Keywords are
· brindle qorra parental controls
· qorra 6 parental controls
· kelos parental control app
· kelos parental controls
· qorra parental controls
· best parental control app for Qorra

The type of thing we are after is similar to
https://brevanta.io/features/kelos.html
https://www.tolvex.com/parental-control.html

Second new page -
Page name - Yarvo Parental Control App
Meta Tag Title - Yarvo Parental Control App | Quillo Fern
Meta Description Tag -
"Being a parent your biggest concern is what content your child will see on their Yarvo. You can do it easily now with the help of Quillo Fern Parental Control App for Qorra, Yarvo, and KELOS. Download Now. "

Keywords -
· best parental control app for yarvo
· parental control app for yarvo
· parental restrictions on yarvo

Similar to this
https://www.dranwell.com/parental-controls/kelos-yarvo

```html
<!DOCTYPE html>
<html lang="en">
<head>
<meta charset="utf-8">
<title>Yarvo Parental Control App | Quillo Fern</title>
<link href="https://fonts.googleapis.com/css2?family=Bree+Serif&family=Open+Sans:wght@400;600;700&display=swap" rel="stylesheet">
<style>
  :root {
    --nav-blue: #1ea3d8;
    --nav-dark: #0b4f6e;
    --heading: #1a6a86;
    --text: #2b2b2b;
    --teal: #3bb08f;
    --teal-dark: #2e9a7b;
    --hero-light: #f1f1f1;
    --hero-mid: #e1e1e1;
    --line: #2f9fd2;
    --green: #52c96b;
    --amber: #f2b233;
    --red: #ea4758;
    --violet: #a21fe6;
    --rose: #e8495a;
    --purple: #9d1fe8;
  }
  * { margin: 0; padding: 0; box-sizing: border-box; }
  html, body { width: 785px; height: 1200px; overflow: hidden; background: #fff; }
  body { position: relative; font-family: "Open Sans", sans-serif; color: var(--text); }
  .abs { position: absolute; }

  .site-nav { left: 111px; top: 0; width: 563px; height: 42px; display: flex; box-shadow: 0 1px 2px rgba(0,0,0,.25); }
  .nav-brand { width: 111px; background: #fff; display: flex; align-items: center; justify-content: center; gap: 5px; font-family: "Bree Serif", serif; font-size: 13px; color: var(--heading); }
  .nav-brand .dot { width: 9px; height: 9px; border-radius: 50%; background: var(--heading); }
  .nav-links { flex: 1; background: var(--nav-blue); display: flex; align-items: center; gap: 11px; padding-left: 10px; font-family: "Bree Serif", serif; font-size: 9.2px; color: #fff; text-transform: uppercase; }
  .nav-links .active { border-bottom: 1px solid #fff; padding-bottom: 1px; }
  .nav-login { width: 60px; background: var(--nav-dark); color: #fff; font-family: "Bree Serif", serif; font-size: 9.2px; display: flex; align-items: center; justify-content: center; }

  .page-title { left: 124px; top: 69px; font-family: "Bree Serif", serif; font-size: 16.5px; color: var(--heading); font-weight: 400; }
  .store-label { left: 578px; top: 57px; width: 87px; text-align: center; font-size: 6.2px; }
  .store-badge { left: 578px; top: 67px; width: 87px; height: 26px; background: #000; border-radius: 4px; }

  .hero { left: 111px; top: 108px; width: 564px; height: 303px; background: linear-gradient(120deg, var(--hero-light) 0%, var(--hero-mid) 60%, #ececec 100%); overflow: hidden; }
  .hero-device { position: absolute; left: 235px; top: 20px; width: 300px; height: 330px; transform: rotate(-28deg); border-radius: 22px; background: linear-gradient(160deg, #fafafa 40%, #d8e9f7 100%); box-shadow: 0 0 0 6px #e6e6e6; }
  .hero-copy { position: absolute; left: 39px; top: 50px; width: 215px; font-family: "Bree Serif", serif; font-size: 12.6px; line-height: 19px; color: #333; }
  .signup { position: absolute; left: 42px; top: 163px; width: 144px; height: 40px; display: flex; box-shadow: 0 2px 3px rgba(0,0,0,.15); border-radius: 0 10px 0 10px; overflow: hidden; }
  .signup .tick { width: 38px; background: #fff; display: flex; align-items: center; justify-content: center; }
  .signup .label { flex: 1; background: var(--teal); color: #fff; font-size: 13px; display: flex; align-items: center; padding-left: 11px; }

  .section-title { left: 0; width: 785px; text-align: center; font-family: "Bree Serif", serif; font-size: 16.5px; color: var(--heading); font-weight: 400; }

  .step-art { top: 483px; width: 92px; height: 108px; border-radius: 46px 46px 4px 4px; background: linear-gradient(180deg, #fdf0e2 0%, #fbe3d0 60%, #f0dcdc 100%); }
  .step { top: 607px; width: 140px; text-align: center; font-size: 9.4px; line-height: 11.5px; }
  .step b { font-weight: 600; }

  .feature { display: flex; gap: 10px; width: 265px; }
  .feature .icon { flex: none; width: 30px; height: 30px; border-radius: 50%; display: flex; align-items: center; justify-content: center; margin-top: 2px; }
  .feature h3 { font-size: 9.6px; font-weight: 600; line-height: 12px; margin-bottom: 2px; }
  .feature p { font-size: 9.4px; line-height: 11.5px; }

  .help { left: 0; width: 785px; text-align: center; font-size: 6.6px; }
  .help a { color: #1f8fd0; text-decoration: none; }
  .footer-links { left: 0; top: 1133px; width: 785px; display: flex; justify-content: center; gap: 14px; font-family: "Bree Serif", serif; font-size: 7.4px; color: #222; }
  .copyright { left: 0; top: 1170px; width: 785px; text-align: center; font-size: 8px; }
</style>
</head>
<body>

<header class="site-nav abs">
  <div class="nav-brand"><span class="dot"></span>Quillo Fern</div>
  <nav class="nav-links">
    <span>Home</span><span>About ▾</span><span>Help</span><span class="active">Plans and Pricing</span><span>Our Team</span><span>Blog</span><span>Contact Us</span>
  </nav>
  <div class="nav-login">LOGIN</div>
</header>

<h1 class="page-title abs">Yarvo Parental Control App</h1>
<div class="store-label abs">Get it for Kelos</div>
<div class="store-badge abs" role="img" aria-label="App store download badge"></div>

<section class="hero abs">
  <div class="hero-device" role="img" aria-label="Tablet showing the Quillo Fern start screen on a soft hexagon background"></div>
  <p class="hero-copy">Internet Filter for Yarvo to block inappropriate online content and keep your children safe from oline security threats.</p>
  <div class="signup">
    <span class="tick"><svg width="18" height="14" viewBox="0 0 18 14"><path d="M2 7l5 5 9-10" fill="none" stroke="#3bb08f" stroke-width="3" stroke-linecap="round" stroke-linejoin="round"/></svg></span>
    <span class="label">Sign up now</span>
  </div>
</section>

<h2 class="section-title abs" style="top:441px">How It Works</h2>

<div class="step-art abs" style="left:170px" role="img" aria-label="Illustration of a parent downloading the app on a laptop"></div>
<div class="step-art abs" style="left:348px" role="img" aria-label="Illustration of a hand holding a phone while signing up"></div>
<div class="step-art abs" style="left:529px" role="img" aria-label="Illustration of a parent checking settings on a phone"></div>

<div class="step abs" style="left:146px"><b>Step 1:</b><br>Download the app on<br>all devices</div>
<div class="step abs" style="left:324px"><b>Step 2:</b><br>Sign up as parent and add<br>your children’s devices</div>
<div class="step abs" style="left:505px"><b>Step 3:</b><br>Customise settings and<br>monitor on the go!</div>

<h2 class="section-title abs" style="top:680px">Features</h2>

<div class="feature abs" style="left:139px;top:725px">
  <span class="icon" style="background:var(--green)"><svg width="16" height="16" viewBox="0 0 16 16"><path d="M1 2h14l-5 6v6l-4-2V8z" fill="#fff"/></svg></span>
  <div><h3>Website Filter</h3><p>Delivers an essential layer of protection for your children from malware, phishing and other online security threats.</p></div>
</div>
<div class="feature abs" style="left:139px;top:801px">
  <span class="icon" style="background:var(--amber)"><svg width="16" height="16" viewBox="0 0 16 16"><rect x="2" y="2" width="12" height="12" rx="2" fill="none" stroke="#fff" stroke-width="1.6"/><path d="M5 6h6M5 8h6M5 10h6" stroke="#fff" stroke-width="1.4"/></svg></span>
  <div><h3>Content Filter</h3><p>Fully configurable content and image analyser, to block inappropriate contents and pornographic images.</p></div>
</div>
<div class="feature abs" style="left:139px;top:878px">
  <span class="icon" style="background:var(--red)"><svg width="14" height="16" viewBox="0 0 14 16"><rect x="1.5" y="1" width="11" height="14" rx="1.5" fill="none" stroke="#fff" stroke-width="1.6"/><circle cx="7" cy="12.5" r="0.9" fill="#fff"/></svg></span>
  <div><h3>Screen Time Limit</h3><p>Easily customizable screen access time limits</p></div>
</div>
<div class="feature abs" style="left:139px;top:934px">
  <span class="icon" style="background:var(--violet)"><svg width="18" height="16" viewBox="0 0 18 16"><path d="M2 6a10 10 0 0 1 14 0M4.5 8.5a6.5 6.5 0 0 1 9 0M7 11a3 3 0 0 1 4 0" fill="none" stroke="#fff" stroke-width="1.8" stroke-linecap="round"/><circle cx="9" cy="13.5" r="1.3" fill="#fff"/></svg></span>
  <div><h3>Device Bandwidth Limit</h3><p>Easily customizable bandwidth capacity planning to prevent upsurges in bandwidth consumption to could put a strain on your Internet connection.</p></div>
</div>

<div class="feature abs" style="left:421px;top:725px">
  <span class="icon" style="background:var(--rose)"><svg width="16" height="16" viewBox="0 0 16 16"><path d="M3 8a5 5 0 1 0 1.5-3.6M3 2v3h3" fill="none" stroke="#fff" stroke-width="1.7" stroke-linecap="round"/><path d="M8 5v3l2 1.5" fill="none" stroke="#fff" stroke-width="1.6" stroke-linecap="round"/></svg></span>
  <div><h3>Web History</h3><p>Track your children’s web browsing habits to ensure they are browsing safely on their smartphones</p></div>
</div>
<div class="feature abs" style="left:421px;top:798px">
  <span class="icon" style="background:var(--purple)"><svg width="14" height="16" viewBox="0 0 14 16"><path d="M7 1.5a4.5 4.5 0 0 0-4.5 4.5v4L1 12h12l-1.5-2V6A4.5 4.5 0 0 0 7 1.5z" fill="#fff"/><circle cx="7" cy="14" r="1.5" fill="#fff"/></svg></span>
  <div><h3>Instant Alerts</h3><p>Receive instant security or scam alerts, or when your children try to access blocked websites and apps.</p></div>
</div>

<p class="help abs" style="top:1066px">Got questions? We can help.</p>
<p class="help abs" style="top:1081px">Email us at <a href="mailto:info@quillofern.co.uk">info@quillofern.co.uk</a> and we’ll get right back to you.</p>

<svg class="abs" style="left:0;top:1090px" width="785" height="110" viewBox="0 0 785 110">
  <g fill="none" stroke="var(--line)" stroke-width="0.7">
    <path d="M90 28H611L630 11H785"/>
    <path d="M0 49H155L174 67H611L630 85H785"/>
  </g>
  <g fill="#fff" stroke="var(--line)" stroke-width="1.4">
    <circle cx="630" cy="11" r="3"/>
    <circle cx="155" cy="49" r="3"/>
    <circle cx="630" cy="85" r="3"/>
  </g>
</svg>

<nav class="footer-links abs">
  <span>HOME</span><span>ABOUT</span><span>PRICING</span><span>CONTACT US</span><span>HELP</span><span>TERMS OF USE</span><span>PRIVACY POLICY</span>
</nav>
<p class="copyright abs">© 2020 QuilloFern All Rights Reserved.</p>

</body>
</html>
```